EPS Recycling Rpt

Our annual recycling rate report needs a tune up. Our organization helps faciltate expanded polystyrene (EPS) recycling and this 4-page report highlights growth trends and useful information to help readers understand the dynamics of EPS recycling. We need a designer that can recreate the brochure we've published over the past several years with some minor adjustments to accomodate new content.

A PDF of the 2012 report is attached. Header text should reflect 2013 in all cases. Please pay close attention to the new placement of the copy as indicated in the Word file (also attached) as it has been significantly modified from the 2012 version. The color pallette for our branding is provided. Contact us with any questions.

```html
<!DOCTYPE html>
<html lang="en">
<head>
<meta charset="utf-8">
<title>EPS Recycling Rate Report 2013</title>
<link rel="stylesheet" href="https://fonts.googleapis.com/css2?family=Montserrat:wght@300;400;600;700&display=swap">
<style>
:root{
  --bronze:#8b6b22;
  --olive:#9aa51c;
  --orange:#ec9a1f;
  --slate:#5d819b;
  --ink:#3a3a3a;
  --paper:#ffffff;
  --stage:#d6d6d6;
  --stage-light:#ffffff;
}
*{box-sizing:border-box;margin:0;padding:0}
html,body{width:1200px;height:871px;overflow:hidden}
body{position:relative;background:var(--stage);font-family:"Montserrat",sans-serif;color:var(--ink)}
.quad{position:absolute;width:600px;height:435px;overflow:hidden}
.quad--cover{left:0;top:0;background:var(--stage-light)}
.quad--stats{left:600px;top:0}
.quad--trend{left:0;top:436px}
.quad--reuse{left:600px;top:436px}
.page{position:absolute;background:var(--paper);overflow:hidden;box-shadow:0 2px 8px rgba(0,0,0,.25)}
.spread{position:absolute;left:40px;top:45px;width:520px;height:345px;background:var(--paper);overflow:hidden;box-shadow:0 3px 10px rgba(0,0,0,.28)}
.spread::after{content:"";position:absolute;left:259px;top:0;width:2px;height:100%;background:linear-gradient(90deg,rgba(0,0,0,.12),rgba(0,0,0,0))}
.abs{position:absolute}
.photo{position:absolute}
.body-copy{position:absolute;font-size:5.5px;line-height:1.5}

/* cover */
.cover{left:175px;top:62px;width:250px;height:315px;border:1px solid #e6e6e6}
.cover__photo{left:-18px;top:22px;width:170px;height:170px;border-radius:50%;background:radial-gradient(circle at 40% 40%,#c9c7d6,#6b6379 55%,#3b3444)}
.cover__org{left:160px;top:54px;font-size:11px;line-height:1.2;color:var(--bronze);font-weight:400}
.cover__tab{left:190px;top:200px;width:60px;height:24px;background:var(--olive);color:#fff;font-size:5px;line-height:1.25;padding:3px 5px;text-transform:uppercase}
.cover__band{left:0;top:224px;width:250px;height:36px;background:var(--bronze)}
.cover__year{left:110px;top:226px;width:75px;text-align:right;font-size:28px;font-weight:300;color:#fff;letter-spacing:1px}

/* stats spread */
.stats__photo-left{left:0;top:0;width:260px;height:120px;background:linear-gradient(135deg,#b99a72,#e8e2d8 55%,#9e9a92)}
.stats__photo-right{left:260px;top:0;width:260px;height:120px;background:linear-gradient(160deg,#c9cdd0,#f2f2f2 50%,#a9adb0)}
.stats__label{left:14px;top:150px;color:#fff;font-size:6px;line-height:1.3;border-left:1px solid #fff;padding-left:4px}
.stats__label b{font-weight:600;font-size:7px;display:block}
.stat{position:absolute;left:14px;color:#fff}
.stat__num{font-size:24px;font-weight:300;line-height:1}
.stat__name{font-size:7px;font-weight:700}
.fig-label{font-size:7px;color:var(--orange);border-left:1px solid var(--orange);padding-left:4px;line-height:1.2}
.fig-label span{display:block;font-size:5px;color:var(--ink)}

/* trend spread */
.trend__photo{left:0;top:0;width:520px;height:345px;background:linear-gradient(170deg,#8f8c80 0%,#cfcbc0 35%,#ece9e2 60%,#b9b5aa 100%)}
.trend__sky{left:330px;top:0;width:190px;height:70px;background:linear-gradient(180deg,#5e86b8,#9dbad8)}
.trend__title-block{left:0;top:0;width:150px;height:150px;background:#1c1c1c}
.trend__kicker{left:12px;top:42px;font-size:13px;font-weight:300;color:#9a9a9a;letter-spacing:.5px}
.trend__title{left:12px;top:60px;font-size:20px;font-weight:700;color:#fff;line-height:1.05}
.trend__intro{left:14px;top:156px;width:230px;color:#222}
.trend__chart{left:14px;top:196px;width:240px;height:138px;background:#fff;box-shadow:0 1px 4px rgba(0,0,0,.2)}
.trend__panel{left:282px;top:90px;width:220px;height:190px;background:var(--slate);padding:12px;color:#fff}
.panel__head{font-size:11px;font-weight:300;color:#d7e2ea;margin-bottom:4px}
.panel__head b{font-weight:700;color:#fff}
.panel__text{font-size:5.5px;line-height:1.5;margin-bottom:14px}

/* reuse spread */
.reuse__kicker{left:16px;top:22px;font-size:14px;font-weight:300;color:var(--olive)}
.reuse__title{left:16px;top:38px;font-size:17px;font-weight:700;color:var(--olive)}
.reuse__ph{position:absolute;height:70px;top:92px}
.reuse__green-copy{color:#fff}
.reuse__others{left:16px;top:262px;font-size:10px;font-weight:300;color:#9a9a9a}
.reuse__others b{font-weight:600;color:var(--olive)}
.brand{position:absolute;font-size:9px;font-weight:600;color:#555}
.seal{position:absolute;width:20px;height:20px;border-radius:50%;background:#777}
.reuse__program{left:284px;top:232px;font-size:8.5px;font-weight:300;color:#8a8a8a}
.reuse__program b{font-weight:600;color:var(--olive)}
.reuse__badge{left:440px;top:246px;width:44px;height:44px;border-radius:50%;background:#e4e8e4}
</style>
</head>
<body>

<!-- Cover -->
<section class="quad quad--cover">
  <article class="page cover">
    <div class="photo cover__photo" role="img" aria-label="Close-up photo of stacked foam tubes"></div>
    <div class="abs cover__org">Foam Recovery<br>Council</div>
    <div class="abs cover__tab">EPS Recycling<br>Rate Report</div>
    <div class="abs cover__band"></div>
    <div class="abs cover__year">2013</div>
  </article>
</section>

<!-- Stats spread -->
<section class="quad quad--stats">
  <article class="spread">
    <div class="photo stats__photo-left" role="img" aria-label="Photo of hands packing foam packaging into a box"></div>
    <div class="photo stats__photo-right" role="img" aria-label="Photo of white foam packaging pieces"></div>
    <svg class="abs" style="left:0;top:0" width="260" height="345" viewBox="0 0 260 345">
      <path d="M0 0 H120 C70 6 30 18 0 34 Z" fill="var(--orange)"/>
      <path d="M0 140 C70 128 170 108 260 98 V345 H0 Z" fill="var(--orange)"/>
    </svg>
    <div class="abs stats__label"><b>Table 1</b>2013 Domestic EPS Recycling<br>millions of pounds</div>
    <div class="stat" style="top:178px"><div class="stat__num">72.8</div><div class="stat__name">Post-Consumer</div></div>
    <div class="stat" style="top:220px"><div class="stat__num">54.5</div><div class="stat__name">Post-Industrial</div></div>
    <div class="stat" style="top:262px"><div class="stat__num">127.3</div><div class="stat__name">Total EPS Recycling</div></div>
    <p class="body-copy" style="left:132px;top:140px;width:112px;color:#fff">Nearly every type of EPS item can be reclaimed and turned into new goods, from trim and frames to fresh packaging.</p>
    <p class="body-copy" style="left:274px;top:134px;width:112px">Since 1990 the rate of post-consumer EPS recycling has grown steadily as more drop-off sites open across the nation.</p>
    <p class="body-copy" style="left:394px;top:134px;width:112px">Commercial collection also expanded this year, with more retailers and makers joining regional take-back programs.</p>
    <div class="abs fig-label" style="left:276px;top:198px">Figure 1<span>Post-Consumer EPS Recycling (1990-2013)</span></div>
    <svg class="abs" style="left:274px;top:178px" width="236" height="130" viewBox="0 0 236 130">
      <g fill="none" stroke="#333" stroke-width=".6"><path d="M14 40 V112 H232"/></g>
      <g fill="var(--orange)">
        <rect x="20" y="108" width="10" height="4"/>
        <rect x="36" y="92" width="10" height="20"/>
        <rect x="52" y="88" width="10" height="24"/>
        <rect x="68" y="86" width="10" height="26"/>
        <rect x="84" y="90" width="10" height="22"/>
        <rect x="100" y="84" width="10" height="28"/>
        <rect x="116" y="82" width="10" height="30"/>
        <rect x="132" y="80" width="10" height="32"/>
        <rect x="148" y="78" width="10" height="34"/>
        <rect x="164" y="74" width="10" height="38"/>
        <rect x="180" y="72" width="10" height="40"/>
        <rect x="196" y="70" width="10" height="42"/>
        <rect x="212" y="40" width="10" height="72"/>
      </g>
      <g font-size="4" fill="#333" font-family="Montserrat, sans-serif">
        <text x="20" y="119">1990</text><text x="52" y="119">1992</text><text x="84" y="119">1994</text>
        <text x="116" y="119">2000</text><text x="148" y="119">2004</text><text x="180" y="119">2008</text><text x="212" y="119">2013</text>
      </g>
    </svg>
  </article>
</section>

<!-- Trend spread -->
<section class="quad quad--trend">
  <article class="spread">
    <div class="photo trend__photo" role="img" aria-label="Photo of a large pile of foam waste at a recycling yard"></div>
    <div class="photo trend__sky" role="img" aria-label="Blue sky above the yard"></div>
    <div class="abs trend__title-block"></div>
    <div class="abs trend__kicker">EPS RECYCLING</div>
    <h1 class="abs trend__title">Stronger<br>Than Ever</h1>
    <p class="body-copy trend__intro">As shown in Figure 2, the rate of EPS recycling continues its steady climb, reaching one of the highest levels yet.</p>
    <div class="abs trend__chart">
      <div class="abs fig-label" style="left:8px;top:6px;color:var(--slate);border-color:var(--slate)">Figure 2<span>Post-Consumer EPS Recycling Rate History (1990-2013)</span></div>
      <svg class="abs" style="left:0;top:26px" width="240" height="112" viewBox="0 0 240 112">
        <g stroke="#d8d8d8" stroke-width=".5">
          <line x1="20" y1="10" x2="232" y2="10"/><line x1="20" y1="26" x2="232" y2="26"/>
          <line x1="20" y1="42" x2="232" y2="42"/><line x1="20" y1="58" x2="232" y2="58"/>
          <line x1="20" y1="74" x2="232" y2="74"/><line x1="20" y1="90" x2="232" y2="90"/>
        </g>
        <polyline fill="none" stroke="var(--slate)" stroke-width="1" points="26,92 44,70 62,64 80,62 98,60 116,52 134,48 152,46 170,32 188,28 206,14 222,6"/>
        <g fill="var(--slate)">
          <circle cx="26" cy="92" r="1.5"/><circle cx="44" cy="70" r="1.5"/><circle cx="62" cy="64" r="1.5"/>
          <circle cx="80" cy="62" r="1.5"/><circle cx="98" cy="60" r="1.5"/><circle cx="116" cy="52" r="1.5"/>
          <circle cx="134" cy="48" r="1.5"/><circle cx="152" cy="46" r="1.5"/><circle cx="170" cy="32" r="1.5"/>
          <circle cx="188" cy="28" r="1.5"/><circle cx="206" cy="14" r="1.5"/><circle cx="222" cy="6" r="1.5"/>
        </g>
        <g font-size="4.5" fill="#555" font-family="Montserrat, sans-serif">
          <text x="8" y="12">40</text><text x="8" y="44">25</text><text x="8" y="76">10</text><text x="10" y="92">0</text>
          <text x="20" y="102">1990</text><text x="56" y="102">1994</text><text x="92" y="102">1998</text>
          <text x="128" y="102">2002</text><text x="164" y="102">2006</text><text x="200" y="102">2010</text><text x="216" y="108">2012</text>
        </g>
      </svg>
    </div>
    <div class="abs trend__panel">
      <h2 class="panel__head">Report <b>Methodology</b></h2>
      <p class="panel__text">Survey data came from processors, converters and collectors who reported the pounds of EPS they reclaimed during the year.</p>
      <h2 class="panel__head">Recycling <b>Criteria</b></h2>
      <p class="panel__text">Only material that was collected, processed and sold for reuse in new products is counted in this total.</p>
    </div>
  </article>
</section>

<!-- Reuse spread -->
<section class="quad quad--reuse">
  <article class="spread">
    <div class="abs reuse__kicker">EPS</div>
    <h1 class="abs reuse__title">Collection &amp; Reuse</h1>
    <div class="reuse__ph" style="left:10px;width:70px;background:linear-gradient(160deg,#8a8678,#c9c2a8)" role="img" aria-label="Photo of volunteers holding foam blocks"></div>
    <div class="reuse__ph" style="left:82px;width:90px;background:linear-gradient(160deg,#6f7a80,#d3d6d4)" role="img" aria-label="Photo of volunteers unloading foam from a car"></div>
    <div class="reuse__ph" style="left:174px;width:86px;background:linear-gradient(160deg,#3e6b3a,#c8d0b8)" role="img" aria-label="Photo of products made from recycled foam"></div>
    <div class="reuse__ph" style="left:262px;width:110px;top:40px;height:50px;background:linear-gradient(160deg,#b8b0a0,#e6e2da)" role="img" aria-label="Photo of a classroom recycling display"></div>
    <div class="reuse__ph" style="left:374px;width:136px;top:40px;height:50px;background:linear-gradient(160deg,#7a6a5e,#dcd6cf)" role="img" aria-label="Photo of students at a collection event"></div>
    <svg class="abs" style="left:0;top:0" width="520" height="345" viewBox="0 0 520 345">
      <path d="M0 168 C90 160 180 150 260 162 V232 C170 222 80 236 0 250 Z" fill="var(--olive)"/>
      <path d="M262 92 H520 V188 C430 178 340 196 262 214 Z" fill="var(--olive)"/>
    </svg>
    <p class="body-copy reuse__green-copy" style="left:14px;top:190px;width:110px">Volunteers gathered bulky foam at local events, easing the load on landfills and feeding new product lines.</p>
    <p class="body-copy reuse__green-copy" style="left:140px;top:184px;width:110px">Drop-off sites make it simple for households to return clean EPS packaging.</p>
    <p class="body-copy reuse__green-copy" style="left:276px;top:104px;width:110px">Schools and retailers also hosted collection days this year with strong turnout.</p>
    <div class="abs reuse__others">Other EPS <b>Recycling Successes</b></div>
    <div class="brand" style="left:20px;top:296px">Vitafare</div>
    <div class="brand" style="left:118px;top:284px">Brightmart</div>
    <div class="brand" style="left:194px;top:270px">Coldstream</div>
    <div class="seal" style="left:130px;top:302px"></div>
    <div class="seal" style="left:208px;top:290px"></div>
    <div class="brand" style="left:28px;top:322px;font-size:7px">Prairie Cuts</div>
    <div class="abs reuse__program">The Packing <b>Fill Return Program</b></div>
    <p class="body-copy" style="left:284px;top:248px;width:140px">The program links shippers with drop-off points where loose fill can be returned and used again.</p>
    <div class="abs reuse__badge"></div>
  </article>
</section>

</body>
</html>
```